Tallow Bright business card

Tallow Bright is a new online life insurance company providing instant quotes and policies to consumers.
Target Market(s)
Target market is both business to business as well as business to consumer
Can think out side of the box- We are an open minded bunch
Industry/Entity Type
Life Insurance
Requirements
Must have
- Our corporate Logo
Double sided
Website www.tallowbright.com.au
Phone Number
Name & Position of each person etc.
Modern font

```html
<!DOCTYPE html>
<html lang="en">
<head>
<meta charset="utf-8">
<title>Tallow Bright business card</title>
<link rel="stylesheet" href="https://fonts.googleapis.com/css2?family=Open+Sans:wght@400;600&display=swap">
<style>
  :root {
    --page: #f2f2f2;
    --card: #ffffff;
    --ink: #1a1a1a;
    --accent: #f07b1d;
    --sky: #dfe6f4;
    --lilac: #e4e1f3;
    --mist: #e2e4e6;
    --photo-dark: #4a4a48;
    --photo-light: #c9c9c4;
  }
  * { margin: 0; padding: 0; box-sizing: border-box; }
  html, body { width: 927px; height: 1200px; overflow: hidden; }
  body {
    background: var(--page);
    font-family: "Open Sans", Arial, sans-serif;
    color: var(--ink);
    position: relative;
  }
  .card {
    position: absolute;
    width: 590px;
    height: 330px;
    background: var(--card);
    overflow: hidden;
    box-shadow: 0 2px 6px rgba(0,0,0,0.12);
  }
  .card--front { left: 100px; top: 140px; }
  .card--back  { left: 237px; top: 630px; }
  .card__shapes { position: absolute; inset: 0; width: 100%; height: 100%; }

  .brand { position: absolute; }
  .brand__name {
    font-weight: 600;
    font-size: 38px;
    line-height: 1;
    color: var(--ink);
    letter-spacing: -0.5px;
  }
  .card--front .brand { left: 258px; top: 66px; }
  .card--back .brand { left: 38px; top: 56px; }
  .card--back .brand__name { font-size: 34px; }

  .front__photo {
    position: absolute;
    left: 0; top: 95px;
    width: 268px; height: 235px;
    background: linear-gradient(135deg, var(--photo-light) 0%, var(--photo-dark) 55%, var(--photo-light) 100%);
  }

  .person { position: absolute; left: 305px; top: 48px; }
  .person__name { font-size: 23px; font-weight: 400; line-height: 1.2; }
  .person__detail { font-size: 15px; line-height: 1.45; padding-left: 2px; }

  .address {
    position: absolute; left: 186px; top: 178px;
    font-size: 15px; line-height: 1.5;
  }
  .website {
    position: absolute; left: 78px; top: 268px;
    font-size: 25px; color: var(--accent);
  }
</style>
</head>
<body>

<section class="card card--front" aria-label="Card front">
  <svg class="card__shapes" viewBox="0 0 590 330" aria-hidden="true">
    <defs>
      <linearGradient id="front-wash" x1="0" y1="0" x2="1" y2="1">
        <stop offset="0" stop-color="#ffffff"/>
        <stop offset="1" stop-color="#eeeff1"/>
      </linearGradient>
    </defs>
    <rect width="590" height="330" fill="url(#front-wash)"/>
    <circle cx="415" cy="-40" r="200" fill="var(--sky)"/>
    <path d="M0 310 C200 300 420 250 590 200 L590 330 L0 330 Z" fill="var(--lilac)"/>
  </svg>
  <div class="front__photo" role="img" aria-label="Close-up photo of an open revolver cylinder"></div>
  <div class="brand">
    <div class="brand__name">Tallow Bright</div>
  </div>
</section>

<section class="card card--back" aria-label="Card back">
  <svg class="card__shapes" viewBox="0 0 590 330" aria-hidden="true">
    <rect width="590" height="330" fill="var(--card)"/>
    <circle cx="410" cy="-20" r="190" fill="var(--sky)"/>
    <path d="M0 250 C180 215 400 200 590 215 L590 330 L0 330 Z" fill="var(--mist)"/>
  </svg>
  <div class="brand">
    <div class="brand__name">Tallow Bright</div>
  </div>
  <div class="person">
    <div class="person__name">Name Surname</div>
    <div class="person__detail">position</div>
    <div class="person__detail">email</div>
    <div class="person__detail">mobile</div>
  </div>
  <div class="address">
    Level 12, 48 Harbour Lane,<br>
    Eastwood, NSW, 2122<br>
    Tel: 1300 555 019
  </div>
  <div class="website">www.tallowbright.com.au</div>
</section>

</body>
</html>
```